Business card for STEADYWAVE

Please design professional business card for IT consulting firm STEADYWAVE INC.
Use logo attached.
Use information from sample qNode business card attached.
replace qnode inc with STEADYWAVE INC.
as well as steadywave.example with steadywave.example

```html
<!DOCTYPE html>
<html lang="en">
<head>
<meta charset="utf-8">
<title>STEADYWAVE Business Card</title>
<link href="https://fonts.googleapis.com/css2?family=Roboto:wght@300;400;500;700;900&display=swap" rel="stylesheet">
<style>
  :root {
    --page-bg: #eceef1;
    --card-bg: #ffffff;
    --ink: #0d0d0d;
    --ink-soft: #3a3a3a;
    --ink-muted: #555555;
    --accent: #7c4fa3;
    --card-shadow: rgba(20, 20, 40, 0.18);
  }
  * { margin: 0; padding: 0; box-sizing: border-box; }
  html, body {
    width: 1200px;
    height: 1200px;
    overflow: hidden;
    background: var(--page-bg);
    font-family: "Roboto", sans-serif;
  }
  .canvas {
    position: relative;
    width: 1200px;
    height: 1200px;
  }
  .card {
    position: absolute;
    left: 233px;
    width: 727px;
    height: 415px;
    background: var(--card-bg);
    box-shadow: 0 4px 14px var(--card-shadow);
  }
  .card--front { top: 165px; }
  .card--back { top: 617px; height: 420px; }

  .wordmark {
    position: absolute;
    display: flex;
    align-items: center;
    font-family: "Roboto", sans-serif;
    font-weight: 900;
    color: var(--ink);
    line-height: 1;
    white-space: nowrap;
  }
  .wordmark__square {
    display: inline-block;
    background: var(--accent);
  }
  .card--front .wordmark {
    left: 43px;
    top: 190px;
    font-size: 36px;
    letter-spacing: 1px;
  }
  .card--front .wordmark__square { width: 13px; height: 13px; margin-left: 9px; }
  .card--back .wordmark {
    left: 148px;
    top: 182px;
    font-size: 60px;
    letter-spacing: 2px;
  }
  .card--back .wordmark__square { width: 22px; height: 22px; margin-left: 14px; }

  .contact {
    position: absolute;
    left: 346px;
    top: 72px;
    color: var(--ink-soft);
  }
  .contact__name {
    font-size: 22px;
    font-weight: 500;
    color: var(--ink);
    letter-spacing: 0.3px;
    line-height: 26px;
    white-space: nowrap;
  }
  .contact__credential { font-size: 14px; font-weight: 500; }
  .contact__role {
    font-size: 15px;
    font-weight: 300;
    letter-spacing: 0.6px;
    color: var(--ink-muted);
    line-height: 20px;
  }
  .contact__lines {
    list-style: none;
    margin-top: 19px;
    font-size: 17px;
    line-height: 31px;
    white-space: nowrap;
  }
  .contact__company {
    margin-top: 5px;
    font-size: 19px;
    font-weight: 500;
    color: var(--ink);
    line-height: 26px;
  }
  .contact__address {
    font-style: normal;
    font-size: 17px;
    line-height: 22px;
    white-space: nowrap;
  }
</style>
</head>
<body>
<main class="canvas">
  <section class="card card--front" aria-label="Card front">
    <div class="wordmark">STEADYWAVE<span class="wordmark__square"></span></div>
    <div class="contact">
      <p class="contact__name">DANIEL HARWOOD, <span class="contact__credential">P. ENG.</span></p>
      <p class="contact__role">GENERAL MANAGER</p>
      <ul class="contact__lines">
        <li>o.(905) 555-0142 EXT.204</li>
        <li>c.(416) 555-0178</li>
        <li>e.dharwood@steadywave.example</li>
        <li>www.steadywave.example</li>
      </ul>
      <p class="contact__company">STEADYWAVE INC.</p>
      <address class="contact__address">
        1280 Lakeview Dr, Suite 204<br>
        Brookfield, Ontario, A1B 2C3, Canada
      </address>
    </div>
  </section>

  <section class="card card--back" aria-label="Card back">
    <div class="wordmark">STEADYWAVE<span class="wordmark__square"></span></div>
  </section>
</main>
</body>
</html>
```